Creative & Professional Business Card for hair salon

We are looking to update our business cards. Our salon is creative, modern, progressive and professional and looking for a design that will reflect this.

```html
<!DOCTYPE html>
<html lang="en">
<head>
<meta charset="utf-8">
<title>Velvet Sky Salon – Business Card</title>
<link rel="stylesheet" href="https://fonts.googleapis.com/css2?family=Open+Sans:wght@300;400;600&display=swap">
<style>
  :root {
    --backdrop: #d9d6d2;
    --card: #0b0b0b;
    --accent: #7fb3cf;
    --accent-soft: #6fa3bf;
    --ink: #f2f2f2;
    --rule: #3a3f44;
  }
  * { margin: 0; padding: 0; box-sizing: border-box; }
  html, body {
    width: 1200px; height: 1000px; overflow: hidden;
    background: var(--backdrop);
    font-family: "Open Sans", Arial, sans-serif;
  }
  .canvas { position: relative; width: 1200px; height: 1000px; }
  .card {
    position: absolute; left: 266px; width: 666px; height: 398px;
    background: var(--card);
    box-shadow: 0 6px 18px rgba(0,0,0,.35);
  }
  .card--front { top: 73px; }
  .card--back { top: 531px; }

  .brand-name {
    position: absolute;
    font-weight: 300;
    color: var(--accent);
    white-space: nowrap;
    letter-spacing: .5px;
  }
  .card--front .brand-name {
    left: 0; right: 0; top: 172px; text-align: center; font-size: 44px;
  }
  .brand-dot {
    display: inline-block; width: 16px; height: 16px; border-radius: 50%;
    background: var(--accent); margin-right: 14px; vertical-align: middle;
  }
  .card--back .brand-name {
    left: 40px; top: 178px; font-size: 25px;
  }
  .card--back .brand-dot { width: 10px; height: 10px; margin-right: 9px; }

  .divider {
    position: absolute; left: 353px; top: 110px; width: 1px; height: 180px;
    background: linear-gradient(to bottom, transparent, var(--rule) 20%, var(--rule) 80%, transparent);
  }
  .contact { position: absolute; left: 380px; top: 118px; color: var(--ink); }
  .contact__name { font-size: 18px; font-weight: 600; color: var(--accent); line-height: 24px; }
  .contact__role { font-size: 15px; color: var(--accent-soft); line-height: 20px; margin-bottom: 10px; }
  .contact__address { font-size: 15px; line-height: 21px; margin-bottom: 6px; }
  .contact__line { display: flex; align-items: center; font-size: 15.5px; line-height: 21px; }
  .contact__line svg { width: 13px; height: 13px; margin-right: 7px; fill: none; stroke: var(--ink); stroke-width: 1.6; }
</style>
</head>
<body>
<div class="canvas">
  <section class="card card--front">
    <div class="brand-name"><span class="brand-dot"></span>Velvet Sky Salon</div>
  </section>

  <section class="card card--back">
    <div class="brand-name"><span class="brand-dot"></span>Velvet Sky Salon</div>
    <div class="divider"></div>
    <div class="contact">
      <p class="contact__name">Daniel Ashworth</p>
      <p class="contact__role">CEO / Owner</p>
      <p class="contact__address">218 Maple Row<br>Riverton, Ohio 45021</p>
      <p class="contact__line">
        <svg viewBox="0 0 16 16"><path d="M2 6c0-2 2-3 6-3s6 1 6 3l-2 1-1-2H5L4 7zM4 8h8l1 5H3z"/></svg>555-204-8817
      </p>
      <p class="contact__line">
        <svg viewBox="0 0 16 16"><rect x="1.5" y="3.5" width="13" height="9"/><path d="M1.5 3.5 8 9l6.5-5.5"/></svg>hello@velvetskysalon.com
      </p>
      <p class="contact__line">
        <svg viewBox="0 0 16 16"><circle cx="8" cy="8" r="6.5"/><path d="M1.5 8h13M8 1.5c3 3.5 3 9.5 0 13M8 1.5c-3 3.5-3 9.5 0 13"/></svg>www.velvetskysalon.com
      </p>
    </div>
  </section>
</div>
</body>
</html>
```